Mine Engineering Consultancy specializing in
* Pit optimization
* Mine Design
* Scheduling
* Mine Rehabilitation

Mining

RVT Mining Pty Ltd
Dennis Holloway
Director/Principle Mining Engineer
Mobile 0418263591
Email dennis.holloway@rvtmining-example.com

```html
<!DOCTYPE html>
<html lang="en">
<head>
<meta charset="utf-8">
<title>RVT Mining Pty Ltd – Business Cards</title>
<link rel="stylesheet" href="https://fonts.googleapis.com/css2?family=Tinos:wght@400&display=swap">
<style>
  :root {
    --bg: #1d1e20;
    --paper: #f4f4f4;
    --brand-blue: #1760b8;
    --brand-blue-deep: #0b4a9c;
    --brand-blue-light: #1b68c4;
    --ink: #333333;
    --band-grey: #6e6e6e;
    --white: #ffffff;
  }
  * { margin: 0; padding: 0; box-sizing: border-box; }
  html, body { width: 1200px; height: 1001px; overflow: hidden; }
  body {
    background: var(--bg);
    position: relative;
    font-family: "Tinos", "Times New Roman", serif;
  }
  .card {
    position: absolute;
    width: 553px;
    height: 334px;
    overflow: hidden;
  }
  .card--front { left: 245px; top: 136px; background: var(--paper); color: var(--ink); }
  .card--back {
    left: 402px; top: 531px;
    background: linear-gradient(180deg, var(--brand-blue-light) 0%, var(--brand-blue-deep) 100%);
    color: var(--white);
  }
  .wordmark {
    position: absolute;
    white-space: nowrap;
    font-weight: 400;
    line-height: 1;
  }
  .card--front .wordmark { left: 34px; top: 58px; font-size: 32px; color: var(--brand-blue); }
  .card--back .wordmark { right: 83px; top: 90px; font-size: 42px; color: var(--white); }
  .rule { position: absolute; height: 1.5px; }
  .card--front .rule { left: 115px; width: 404px; top: 100px; background: #555; }
  .card--back .rule { left: 235px; right: 0; top: 148px; background: var(--white); height: 2px; }
  .tagline {
    position: absolute;
    right: 34px; top: 109px;
    font-size: 15px;
    color: var(--ink);
    white-space: nowrap;
  }
  .person { position: absolute; left: 34px; top: 243px; }
  .person__name { font-size: 22px; color: var(--brand-blue); letter-spacing: 0.2px; line-height: 1.1; }
  .person__role { font-size: 14.5px; color: var(--ink); margin-top: 2px; }
  .contact {
    position: absolute;
    right: 34px; top: 248px;
    text-align: right;
    font-size: 13.5px;
    line-height: 17px;
    color: var(--ink);
    white-space: nowrap;
  }
  .contact__label { color: var(--brand-blue); }
  .band { position: absolute; left: 0; bottom: 0; width: 553px; height: 17px; }
  .services {
    position: absolute;
    right: 83px; top: 177px;
    list-style: none;
    text-align: right;
    font-size: 16px;
    line-height: 29.5px;
    white-space: nowrap;
  }
</style>
</head>
<body>
  <section class="card card--front" aria-label="Business card front">
    <div class="wordmark">RVT Mining Pty Ltd</div>
    <div class="rule"></div>
    <p class="tagline">Pit optimization · Mine Design · Scheduling · Mine Rehabilitation</p>
    <div class="person">
      <div class="person__name">DENNIS HOLLOWAY</div>
      <div class="person__role">Director / Principle Mining Engineer</div>
    </div>
    <div class="contact">
      <div><span class="contact__label">T:</span> 0418263591</div>
      <div><span class="contact__label">E:</span> dennis.holloway@rvtmining-example.com</div>
    </div>
    <svg class="band" viewBox="0 0 553 17" aria-hidden="true">
      <polygon points="0,0 277,0 286,8.5 277,17 0,17" fill="var(--brand-blue)"/>
      <polygon points="280,0 553,0 553,17 280,17 289,8.5" fill="var(--band-grey)"/>
    </svg>
  </section>

  <section class="card card--back" aria-label="Business card back">
    <div class="wordmark">RVT Mining Pty Ltd</div>
    <div class="rule"></div>
    <ul class="services">
      <li>Pit optimization</li>
      <li>Mine Design</li>
      <li>Scheduling</li>
      <li>Mine Rehabilitation</li>
    </ul>
  </section>
</body>
</html>
```